Pemberton Dialworks Business Card Design

Double Sided Business Card Design for a Locksmith company specializing in Safecracking, safe & vault service.

```html
<!DOCTYPE html>
<html lang="en">
<head>
<meta charset="utf-8">
<title>Pemberton Dialworks – Business Card</title>
<link rel="stylesheet" href="https://fonts.googleapis.com/css2?family=Montserrat:wght@400;500;800&display=swap">
<style>
  :root {
    --card-black: #231f20;
    --brand-green: #1f7a3a;
    --accent-grey: #c4c6c9;
    --ink-white: #ffffff;
    --divider: #6b6b6b;
    --page: #e9e7e4;
  }
  html, body {
    margin: 0;
    width: 1200px;
    height: 900px;
    overflow: hidden;
    background: var(--page);
    font-family: "Montserrat", sans-serif;
  }
  .sheet {
    width: 1200px;
    height: 900px;
    display: flex;
    flex-direction: column;
    align-items: center;
    justify-content: center;
    gap: 40px;
  }
  .card {
    position: relative;
    width: 700px;
    height: 400px;
    background: var(--card-black);
    overflow: hidden;
    box-shadow: 0 6px 18px rgba(0,0,0,.18);
    color: var(--ink-white);
  }
  .brand {
    display: flex;
    align-items: center;
    gap: 16px;
  }
  .brand-dot {
    flex: none;
    border-radius: 50%;
    background: var(--brand-green);
  }
  .brand-name {
    font-weight: 800;
    text-transform: uppercase;
    color: var(--ink-white);
    line-height: 1.02;
    letter-spacing: .04em;
    margin: 0;
  }

  /* Front */
  .card-front .brand {
    position: absolute;
    left: 60px;
    top: 154px;
  }
  .card-front .brand-dot { width: 92px; height: 92px; }
  .card-front .brand-name { font-size: 32px; }
  .service-imagery {
    position: absolute;
    top: 0;
    right: 0;
    width: 230px;
    height: 400px;
    background: linear-gradient(160deg, var(--accent-grey) 0%, #6f7a74 45%, var(--brand-green) 100%);
  }

  /* Back */
  .card-back .brand {
    position: absolute;
    left: 0;
    right: 0;
    top: 52px;
    justify-content: center;
  }
  .card-back .brand-dot { width: 70px; height: 70px; }
  .card-back .brand-name { font-size: 26px; }
  .holder-name {
    position: absolute;
    left: 0;
    right: 0;
    top: 168px;
    text-align: center;
    font-size: 22px;
    font-weight: 400;
    letter-spacing: .06em;
    margin: 0;
  }
  .contact-row {
    position: absolute;
    left: 40px;
    right: 40px;
    bottom: 38px;
    display: grid;
    grid-template-columns: 1fr 1fr 1fr;
  }
  .contact-item {
    display: flex;
    flex-direction: column;
    align-items: center;
    gap: 14px;
    padding: 14px 0;
    font-size: 15px;
    letter-spacing: .04em;
  }
  .contact-item + .contact-item { border-left: 1px solid var(--divider); }
  .contact-icon {
    width: 30px;
    height: 30px;
    border-radius: 50%;
    background: var(--brand-green);
    display: flex;
    align-items: center;
    justify-content: center;
  }
  .contact-icon svg { width: 16px; height: 16px; }
</style>
</head>
<body>
<main class="sheet">

  <section class="card card-front" aria-label="Card front">
    <div class="brand">
      <span class="brand-dot"></span>
      <h1 class="brand-name">Pemberton<br>Dialworks</h1>
    </div>
    <div class="service-imagery" role="img" aria-label="Decorative cluster of framed photos showing safe opening and door lock servicing"></div>
  </section>

  <section class="card card-back" aria-label="Card back">
    <div class="brand">
      <span class="brand-dot"></span>
      <p class="brand-name">Pemberton<br>Dialworks</p>
    </div>
    <p class="holder-name">Name Last Name</p>
    <div class="contact-row">
      <div class="contact-item">
        <span class="contact-icon">
          <svg viewBox="0 0 16 16"><path d="M3.5 1.5l2.5 3-1.4 1.6c.9 2 2.4 3.5 4.4 4.4l1.6-1.4 3 2.5-1.6 2.4C6.6 13.6 2.4 9.4 1.1 3.1z" fill="none" stroke="#fff" stroke-width="1.2" stroke-linejoin="round"/></svg>
        </span>
        <span>0123 456 789</span>
      </div>
      <div class="contact-item">
        <span class="contact-icon">
          <svg viewBox="0 0 16 16" fill="none" stroke="#fff" stroke-width="1.1"><circle cx="8" cy="8" r="6.5"/><ellipse cx="8" cy="8" rx="3" ry="6.5"/><path d="M1.5 8h13M2.5 4.5h11M2.5 11.5h11"/></svg>
        </span>
        <span>www.yoursite.com</span>
      </div>
      <div class="contact-item">
        <span class="contact-icon">
          <svg viewBox="0 0 16 16" fill="none" stroke="#fff" stroke-width="1.2"><rect x="1.5" y="3.5" width="13" height="9"/><path d="M1.5 3.5L8 9l6.5-5.5"/></svg>
        </span>
        <span>youremail@mail.com</span>
      </div>
    </div>
  </section>

</main>
</body>
</html>
```